Criação de Kit Layout de Posts para Redes Sociais (/vitaliscursos, Instagram e etc) para Educação & Cursos
" Cursos Técnicos na área de saúde e Educação do Ensino fundamental ao Ensino Médio "

```html
<!DOCTYPE html>
<html lang="pt-BR">
<head>
<meta charset="UTF-8">
<title>Curso de APH – Vitalis Curso e Escola</title>
<link rel="stylesheet" href="https://fonts.googleapis.com/css2?family=Oswald:wght@600&family=Roboto+Condensed:wght@700&display=swap">
<style>
  :root {
    --brand-blue: #1b5cb8;
    --brand-navy: #123a7a;
    --white: #ffffff;
    --photo-dark: #1d2738;
    --photo-mid: #4a5466;
    --photo-warm: #d9822b;
    --photo-light: #b9bec6;
  }
  * { margin: 0; padding: 0; box-sizing: border-box; }
  html, body { width: 1200px; height: 1200px; overflow: hidden; background: var(--white); }
  .post {
    position: relative;
    width: 1200px;
    height: 1200px;
    overflow: hidden;
    font-family: "Roboto Condensed", "Arial Narrow", sans-serif;
    color: var(--white);
  }
  .hero-photo {
    position: absolute;
    inset: 0;
    background:
      radial-gradient(ellipse 380px 300px at 820px 560px, rgba(217,130,43,0.55), transparent 70%),
      radial-gradient(ellipse 300px 260px at 1050px 250px, rgba(185,190,198,0.7), transparent 70%),
      radial-gradient(ellipse 360px 420px at 260px 620px, rgba(74,84,102,0.7), transparent 70%),
      linear-gradient(135deg, var(--photo-dark) 0%, var(--photo-mid) 45%, var(--photo-dark) 100%);
  }
  .headline {
    position: absolute;
    left: 96px;
    top: 88px;
    font-family: "Oswald", "Arial Narrow", sans-serif;
    font-weight: 600;
    font-size: 58px;
    line-height: 65px;
    text-transform: uppercase;
    text-shadow: 0 3px 10px rgba(0,0,0,0.55);
  }
  .lead {
    position: absolute;
    left: 96px;
    top: 342px;
    font-size: 28px;
    line-height: 37px;
    font-weight: 700;
    text-transform: uppercase;
    text-shadow: 0 2px 8px rgba(0,0,0,0.6);
  }
  .footer-wave { position: absolute; inset: 0; }
  .contacts {
    position: absolute;
    left: 68px;
    top: 1032px;
    display: grid;
    grid-template-columns: 330px 300px;
    row-gap: 18px;
    font-size: 31px;
    font-weight: 700;
  }
  .contact { display: flex; align-items: center; gap: 16px; }
  .contact svg { width: 30px; height: 30px; flex: none; }
  .dot { width: 22px; height: 22px; border-radius: 50%; background: var(--white); flex: none; margin: 0 4px; }
  .brand-seal {
    position: absolute;
    left: 751px;
    top: 744px;
    width: 408px;
    height: 408px;
    border-radius: 50%;
    background: var(--brand-navy);
    border: 10px solid var(--white);
    display: flex;
    flex-direction: column;
    align-items: center;
    justify-content: center;
    text-align: center;
    font-family: "Oswald", "Arial Narrow", sans-serif;
    font-weight: 600;
    color: var(--white);
    text-transform: uppercase;
  }
  .brand-seal .name { font-size: 64px; line-height: 1.05; letter-spacing: 2px; }
  .brand-seal .tagline { font-size: 34px; line-height: 1.3; letter-spacing: 3px; }
</style>
</head>
<body>
<main class="post">
  <div class="hero-photo" role="img" aria-label="Fotografia de socorristas de uniforme imobilizando um paciente em uma prancha com cintos laranja"></div>

  <h1 class="headline">Curso de APH<br>Atendimento<br>Pré Hospitalar</h1>

  <p class="lead">Oferecemos a melhor<br>infraestrutura para<br>seu futuro! Saiba mais<br>sobre o curso, entre<br>em contato!</p>

  <svg class="footer-wave" viewBox="0 0 1200 1200" aria-hidden="true">
    <path d="M0 935 C 320 985, 720 900, 1200 835 L1200 1200 L0 1200 Z" fill="var(--white)"/>
    <path d="M0 972 C 330 1010, 730 930, 1200 868 L1200 1200 L0 1200 Z" fill="var(--brand-blue)"/>
  </svg>

  <div class="contacts">
    <div class="contact">
      <svg viewBox="0 0 24 24" aria-hidden="true"><path fill="#fff" d="M6.6 10.8a15.1 15.1 0 0 0 6.6 6.6l2.2-2.2c.3-.3.7-.4 1-.2 1.1.4 2.3.6 3.6.6.6 0 1 .4 1 1V20c0 .6-.4 1-1 1A17 17 0 0 1 3 4c0-.6.4-1 1-1h3.5c.6 0 1 .4 1 1 0 1.3.2 2.5.6 3.6.1.3 0 .7-.2 1z"/></svg>
      <span>(00) 0000-0000</span>
    </div>
    <div class="contact"><span class="dot"></span><span>@vitaliscursos</span></div>
    <div class="contact">
      <svg viewBox="0 0 24 24" aria-hidden="true"><path fill="#fff" d="M6.6 10.8a15.1 15.1 0 0 0 6.6 6.6l2.2-2.2c.3-.3.7-.4 1-.2 1.1.4 2.3.6 3.6.6.6 0 1 .4 1 1V20c0 .6-.4 1-1 1A17 17 0 0 1 3 4c0-.6.4-1 1-1h3.5c.6 0 1 .4 1 1 0 1.3.2 2.5.6 3.6.1.3 0 .7-.2 1z"/></svg>
      <span>(00) 9 9999-9999</span>
    </div>
    <div class="contact"><span class="dot"></span><span>/vitaliscursos</span></div>
  </div>

  <div class="brand-seal">
    <span class="name">Vitalis</span>
    <span class="tagline">Curso e Escola</span>
  </div>
</main>
</body>
</html>
```